Business Card for my New Brokerage

Looking to get a business card design for my new Real Estate Brokerage.
I want it with Picture, Phone Number, Email, Website, Office Address
Name and Designation. Please add logo too.

Target Market(s)

Real Estate Investors or Home Buyers

Industry/Entity Type

Real Estate

Contact Information for Business Card

Name, Email, Phone Number, website, email, office address

Colors
EB3D1F
EC4F4E
F09395
F8D3D4
FCEDEE

Requirements
Must have
• Minimalistic, Clean, Modern, Photo
Nice to have
• White and Red Colors

```html
<!DOCTYPE html>
<html lang="en">
<head>
<meta charset="utf-8">
<title>Beacon Realty Inc – Business Card</title>
<link href="https://fonts.googleapis.com/css2?family=Montserrat:wght@400;500;600;700;800&display=swap" rel="stylesheet">
<style>
  :root {
    --brand-red: #dd0000;
    --deep-red: #b80000;
    --gold: #d6ab4c;
    --gold-light: #f3dc8f;
    --ink: #1b1b1b;
    --white: #ffffff;
    --paper: #f6f6f8;
    --page: #ffffff;
  }
  * { box-sizing: border-box; margin: 0; padding: 0; }
  html, body {
    width: 797px; height: 1200px; overflow: hidden;
    background: var(--page);
    font-family: "Montserrat", sans-serif;
  }
  .canvas { position: relative; width: 797px; height: 1200px; }

  .card {
    position: absolute; left: 98px; width: 600px; height: 343px;
    overflow: hidden;
    box-shadow: 0 10px 28px rgba(0,0,0,.18);
  }
  .card-front { top: 227px; background: var(--brand-red); }
  .card-back  { top: 630px; background: var(--paper); }

  .card-shapes { position: absolute; inset: 0; width: 100%; height: 100%; }

  /* Front */
  .front-glow {
    position: absolute; right: 0; bottom: 0; width: 260px; height: 150px;
    background: radial-gradient(ellipse at 100% 100%, var(--deep-red) 0%, rgba(184,0,0,0) 70%);
  }
  .portrait {
    position: absolute; left: 71px; top: 47px; width: 114px; height: 138px;
    border: 3px solid var(--white);
    background: linear-gradient(160deg, #d4d4d4 0%, #b9b9b9 55%, #2a3142 100%);
  }
  .brand-front {
    position: absolute; left: 212px; top: 46px;
    color: var(--white); font-weight: 700; line-height: 1;
  }
  .brand-front .brand-name { font-size: 34px; letter-spacing: .5px; }
  .brand-front .brand-sub  { display: block; font-size: 11px; letter-spacing: 3px; margin: 5px 0 0 30px; }

  .agent-name {
    position: absolute; left: 212px; top: 118px;
    color: var(--white); font-weight: 800; font-size: 35px; letter-spacing: .5px; line-height: 1;
  }
  .agent-role {
    position: absolute; left: 212px; top: 160px;
    color: var(--white); font-weight: 500; font-size: 22px; line-height: 1;
  }

  .contact {
    position: absolute; display: flex; align-items: center; gap: 9px;
    color: var(--white); font-weight: 600; font-size: 16.5px; line-height: 1;
  }
  .contact svg { width: 28px; height: 30px; flex: none; }
  .contact-phone-1 { left: 72px;  top: 218px; }
  .contact-phone-2 { left: 72px;  top: 257px; }
  .contact-email   { left: 300px; top: 218px; }
  .contact-web     { left: 300px; top: 257px; }
  .contact-divider {
    position: absolute; left: 278px; top: 221px; width: 1px; height: 62px;
    background: rgba(255,255,255,.85);
  }

  .address {
    position: absolute; left: 0; right: 0; top: 308px;
    display: flex; justify-content: center; align-items: center; gap: 8px;
    color: var(--white); font-weight: 600; font-size: 14px; line-height: 1;
    padding-right: 70px;
  }
  .address svg { width: 11px; height: 15px; }

  /* Back */
  .back-haze {
    position: absolute; inset: 0;
    background:
      radial-gradient(ellipse at 0% 0%, #d9d9de 0%, rgba(217,217,222,0) 45%),
      radial-gradient(ellipse at 100% 0%, #d9d9de 0%, rgba(217,217,222,0) 45%),
      linear-gradient(180deg, #f1f1f4 0%, #fbfbfc 100%);
  }
  .brand-back {
    position: absolute; left: 0; right: 0; top: 100px; text-align: center;
    color: var(--brand-red); font-weight: 800; line-height: 1;
  }
  .brand-back .brand-name { display: block; font-size: 76px; letter-spacing: 1px; }
  .brand-back .brand-sub  { display: block; font-size: 22px; letter-spacing: 6px; margin-top: 16px; }

  .back-url {
    position: absolute; left: 0; right: 0; top: 259px; text-align: center;
    color: var(--white); font-weight: 700; font-size: 22px; letter-spacing: 1.5px; line-height: 1;
  }
</style>
</head>
<body>
<main class="canvas">

  <!-- Front side -->
  <section class="card card-front" aria-label="Business card front">
    <div class="front-glow"></div>
    <svg class="card-shapes" viewBox="0 0 600 343" aria-hidden="true">
      <defs>
        <linearGradient id="goldRule" x1="0" x2="1">
          <stop offset="0" stop-color="#d6ab4c"/>
          <stop offset="1" stop-color="#f0cf72"/>
        </linearGradient>
      </defs>
      <line x1="439" y1="176" x2="600" y2="176" stroke="url(#goldRule)" stroke-width="1.5"/>
      <polygon points="0,331 70,331 93,301 534,301 557,331 600,331 600,343 0,343" fill="#1b1b1b"/>
    </svg>

    <div class="portrait" role="img" aria-label="Portrait photo of the agent"></div>

    <div class="brand-front">
      <span class="brand-name">BEACON</span>
      <span class="brand-sub">REALTY INC</span>
    </div>

    <h1 class="agent-name">DANIEL HAYES</h1>
    <p class="agent-role">Creative director</p>

    <div class="contact contact-phone-1">
      <svg viewBox="0 0 28 30" aria-hidden="true">
        <polygon points="14,1 27,8 27,22 14,29 1,22 1,8" fill="#d6ab4c"/>
        <path d="M10 9c1-1 2 0 3 2s0 2-1 3c1 2 2 3 4 4 1-1 1-2 3-1s3 2 2 3c-1 2-3 2-5 1-3-1-6-4-7-7-1-2-1-4 1-5z" fill="#1b1b1b"/>
      </svg>
      <span>000.2468.1357</span>
    </div>
    <div class="contact contact-phone-2">
      <svg viewBox="0 0 28 30" aria-hidden="true">
        <polygon points="14,1 27,8 27,22 14,29 1,22 1,8" fill="#d6ab4c"/>
        <path d="M10 9c1-1 2 0 3 2s0 2-1 3c1 2 2 3 4 4 1-1 1-2 3-1s3 2 2 3c-1 2-3 2-5 1-3-1-6-4-7-7-1-2-1-4 1-5z" fill="#1b1b1b"/>
      </svg>
      <span>000.9753.8642</span>
    </div>

    <div class="contact-divider"></div>

    <div class="contact contact-email">
      <svg viewBox="0 0 28 30" aria-hidden="true">
        <polygon points="14,1 27,8 27,22 14,29 1,22 1,8" fill="#d6ab4c"/>
        <rect x="7" y="10" width="14" height="10" fill="none" stroke="#1b1b1b" stroke-width="1.6"/>
        <path d="M7 10l7 6 7-6M7 20l5-5M21 20l-5-5" fill="none" stroke="#1b1b1b" stroke-width="1.4"/>
      </svg>
      <span>hello@beaconmail.com</span>
    </div>
    <div class="contact contact-web">
      <svg viewBox="0 0 28 30" aria-hidden="true">
        <polygon points="14,1 27,8 27,22 14,29 1,22 1,8" fill="#d6ab4c"/>
        <g fill="none" stroke="#1b1b1b" stroke-width="1.3">
          <circle cx="14" cy="15" r="7"/>
          <ellipse cx="14" cy="15" rx="3" ry="7"/>
          <path d="M7 15h14M8.5 11h11M8.5 19h11"/>
        </g>
      </svg>
      <span>www.beaconhomes.com</span>
    </div>

    <p class="address">
      <svg viewBox="0 0 11 15" aria-hidden="true">
        <path d="M5.5 0a5.5 5.5 0 0 1 5.5 5.5C11 9.5 5.5 15 5.5 15S0 9.5 0 5.5A5.5 5.5 0 0 1 5.5 0z" fill="#d6ab4c"/>
        <circle cx="5.5" cy="5.5" r="2" fill="#1b1b1b"/>
      </svg>
      118 Marlow Avenue, Brookdale NY 54321
    </p>
  </section>

  <!-- Back side -->
  <section class="card card-back" aria-label="Business card back">
    <div class="back-haze"></div>

    <div class="brand-back">
      <span class="brand-name">BEACON</span>
      <span class="brand-sub">REALTY INC</span>
    </div>

    <svg class="card-shapes" viewBox="0 0 600 343" aria-hidden="true">
      <defs>
        <linearGradient id="goldBand" x1="0" x2="1">
          <stop offset="0" stop-color="#d6ab4c"/>
          <stop offset=".5" stop-color="#f3dc8f"/>
          <stop offset="1" stop-color="#d6ab4c"/>
        </linearGradient>
      </defs>
      <rect x="0" y="265" width="120" height="16" fill="url(#goldBand)"/>
      <rect x="478" y="265" width="122" height="16" fill="url(#goldBand)"/>
      <polygon points="112,254 487,254 469,287 131,287" fill="#dd0000"/>
    </svg>

    <p class="back-url">www.beaconrealty.com</p>
  </section>

</main>
</body>
</html>
```